Zentro - revolutionary mobile payment

The app is a P2P money trasfert, without the using of credit card or bank circuits it can transfer electronic money from one person to another consumers simply and immediatelly.
You can use the color you want, but the message we need to transert to consumer is simplicity, safety and coolness.
In attach the logo of the company and the wireframe of thre page of the app.
The goal is to design the page of the app with a clear, simple and intuitive graphic.
Updates

I have upgrade the brief with important information and detail, many thanks

Target Market(s)

all the people

Industry/Entity Type

Credit Card

Requirements
Must have
• You have to design one icon for each button in the first page, (shop is: where to shop)
in the second one a new intuitive image (instead of the hand) that let the user to understand that with a simple swipe he can process the payment
Nice to have
• You can include or esxclude what you want or belive can improve user experience of the app
Should not have
• too much color, too much button or information

```html
<!DOCTYPE html>
<html lang="it">
<head>
<meta charset="utf-8">
<title>Zentro – app screens</title>
<link rel="stylesheet" href="https://fonts.googleapis.com/css2?family=Jost:wght@300;400;500&display=swap">
<style>
  :root{
    --canvas-top:#5a5d62;
    --canvas-bottom:#2c2e32;
    --blue-deep:#0f3262;
    --blue-mid:#1a4c8c;
    --blue-tile:#17437d;
    --blue-accent:#1f63c0;
    --blue-bright:#3f95ea;
    --blue-light:#8cc2f5;
    --blue-pale:#b8dafa;
    --ring:#4da3f2;
    --white:#ffffff;
    --text-soft:#cfe3fb;
  }
  *{box-sizing:border-box;margin:0;padding:0}
  html,body{width:1200px;height:1200px;overflow:hidden}
  body{
    background:linear-gradient(160deg,var(--canvas-top),var(--canvas-bottom));
    font-family:"Jost",sans-serif;color:var(--white);position:relative;
  }
  .screen{
    position:absolute;width:320px;height:560px;overflow:hidden;border-radius:6px;
    background:linear-gradient(170deg,var(--blue-mid) 0%,var(--blue-deep) 100%);
    box-shadow:0 20px 50px rgba(0,0,0,.45);
  }
  .screen--home{left:140px;top:20px}
  .screen--shop{left:740px;top:20px}
  .screen--buy{left:140px;top:620px}
  .screen--balance{left:740px;top:620px}

  .status-bar{position:absolute;left:0;top:0;width:100%;height:22px;display:flex;
    align-items:center;justify-content:space-between;padding:0 10px;font-size:10px;font-weight:400}
  .status-bar .signal{letter-spacing:1px}
  .status-bar .battery{display:flex;align-items:center;gap:4px}
  .battery-icon{width:20px;height:9px;border:1px solid var(--white);border-radius:2px;position:relative}
  .battery-icon::after{content:"";position:absolute;left:1px;top:1px;width:4px;height:5px;background:var(--white)}

  .top-bar{position:absolute;top:26px;left:0;width:100%;height:30px}
  .top-bar .icon-user{position:absolute;left:14px;top:4px}
  .top-bar .icon-gear{position:absolute;right:14px;top:4px}
  .top-bar .menu-caret{position:absolute;left:152px;top:8px}
  .back-link{position:absolute;left:0;width:100%;top:4px;text-align:center;font-size:15px;font-weight:300;color:var(--text-soft)}

  .welcome{position:absolute;top:72px;width:100%;text-align:center;font-size:19px;font-weight:300;letter-spacing:1px}
  .brand{display:flex;align-items:center;justify-content:center;gap:8px;font-weight:500;color:var(--white)}
  .brand .brand-dot{border:2px solid var(--white);border-radius:50%}
  .brand--large{position:absolute;top:102px;width:100%;font-size:30px}
  .brand--large .brand-dot{width:28px;height:28px}
  .brand--small{position:absolute;bottom:40px;left:0;width:100%;font-size:18px}
  .brand--small .brand-dot{width:18px;height:18px}
  .brand-rule{position:absolute;top:150px;left:140px;width:40px;height:2px;background:var(--white)}

  .menu-graphic{position:absolute;left:0;top:0}
  .menu-label{font-family:"Jost",sans-serif;font-size:13px;font-weight:300;fill:var(--white);text-anchor:middle}

  .footer-bars{position:absolute;bottom:10px;left:0;width:100%;height:6px;display:flex;gap:4px;padding:0 0 0 40px}
  .footer-bars span{flex:1;background:var(--blue-bright)}
  .footer-bars span:last-child{background:var(--blue-light)}

  /* form screens */
  .title-row{position:absolute;top:70px;left:0;height:48px;width:100%;display:flex;align-items:center}
  .title-row .title-icon{width:60px;display:flex;justify-content:center}
  .title-row .divider{width:1px;height:32px;background:var(--text-soft);opacity:.6}
  .title-row .title{padding-left:12px;font-size:24px;font-weight:300}
  .block{position:absolute;display:flex;align-items:center;justify-content:center}
  .tab-phone{left:90px;top:124px;width:100px;height:40px;background:var(--blue-bright);font-size:15px}
  .field-phone{left:190px;top:124px;width:130px;height:40px;background:var(--white);color:var(--blue-deep);justify-content:flex-end;padding-right:16px;font-size:18px}
  .corner-tile{left:230px;top:74px;width:90px;height:46px;background:var(--blue-pale)}
  .prefix{left:40px;top:168px;width:80px;height:38px;background:var(--blue-accent);font-size:15px}
  .field-amount{left:0;top:208px;width:260px;height:40px;background:var(--white);color:var(--blue-deep);justify-content:flex-start;padding-left:50px;font-size:20px}
  .notes-hint{position:absolute;left:14px;top:254px;font-size:11px;font-weight:300;color:var(--text-soft)}
  .keypad{position:absolute;left:14px;top:276px;width:292px;display:grid;grid-template-columns:repeat(3,1fr);gap:2px}
  .key{height:50px;background:rgba(31,99,192,.35);display:flex;flex-direction:column;align-items:center;justify-content:center;font-size:18px;font-weight:300}
  .key small{font-size:10px;letter-spacing:1px}
  .key--active{background:var(--blue-bright)}
  .key--empty{background:transparent}

  .balance-tile{left:180px;top:70px;width:140px;height:46px;background:var(--blue-bright);justify-content:flex-end;padding-right:16px;font-size:26px;font-weight:300}
  .band{left:110px;top:118px;width:210px;height:40px;background:var(--blue-accent)}
  .currency{left:40px;top:160px;width:70px;height:40px;background:var(--blue-accent);font-size:20px}
  .period{left:110px;top:160px;width:210px;height:40px;background:rgba(31,99,192,.55);font-size:12px;font-weight:300}
  .tx-row{left:14px;width:306px;height:44px;justify-content:flex-start;gap:12px;padding-left:14px;font-size:13px}
  .tx-row .amount{margin-left:auto;margin-right:34px}
  .tx-row--in{top:206px;background:var(--blue-pale);color:var(--blue-deep)}
  .tx-row--out{top:252px;background:var(--blue-bright)}
  .caret{position:absolute;right:12px;top:50%;margin-top:-4px;width:0;height:0;border-left:5px solid transparent;border-right:5px solid transparent;border-top:7px solid currentColor}
</style>
</head>
<body>

<!-- Shared symbol definitions -->
<svg width="0" height="0" style="position:absolute" aria-hidden="true">
  <defs>
    <symbol id="i-user" viewBox="0 0 20 20"><circle cx="10" cy="6" r="4" fill="none" stroke="currentColor" stroke-width="1.4"/><path d="M2 18c0-4 3.5-6 8-6s8 2 8 6z" fill="none" stroke="currentColor" stroke-width="1.4"/></symbol>
    <symbol id="i-gear" viewBox="0 0 20 20"><circle cx="10" cy="10" r="3" fill="none" stroke="currentColor" stroke-width="1.6"/><circle cx="10" cy="10" r="6.5" fill="none" stroke="currentColor" stroke-width="3" stroke-dasharray="3 2.1"/></symbol>
    <symbol id="i-hand" viewBox="0 0 24 24"><path d="M9 21v-4l-3-4c-.6-1 .6-2 1.5-1.2L9 13V5a1.3 1.3 0 0 1 2.6 0v6l6 1.2c1 .2 1.4 1 1.3 2l-.8 6.8" fill="none" stroke="currentColor" stroke-width="1.4" stroke-linejoin="round"/><path d="M5 4l2 2M10 1v2M15 4l-2 2" stroke="currentColor" stroke-width="1.4"/></symbol>
    <symbol id="i-cart" viewBox="0 0 24 24"><path d="M2 4h3l2.5 11h11l2-8H6.5" fill="none" stroke="currentColor" stroke-width="1.5" stroke-linejoin="round"/><circle cx="9" cy="19" r="1.6" fill="none" stroke="currentColor" stroke-width="1.4"/><circle cx="17" cy="19" r="1.6" fill="none" stroke="currentColor" stroke-width="1.4"/></symbol>
    <symbol id="i-house" viewBox="0 0 24 24"><path d="M3 12l9-8 9 8M6 10v10h12V10M10 20v-5h4v5" fill="none" stroke="currentColor" stroke-width="1.6" stroke-linejoin="round"/></symbol>
    <symbol id="i-user-clock" viewBox="0 0 28 24"><circle cx="10" cy="7" r="4.5" fill="none" stroke="currentColor" stroke-width="1.4"/><path d="M1 22c0-5 4-7 9-7 2 0 3.5.3 5 1" fill="none" stroke="currentColor" stroke-width="1.4"/><circle cx="21" cy="17" r="5" fill="none" stroke="currentColor" stroke-width="1.4"/><path d="M21 14.5V17h2" stroke="currentColor" stroke-width="1.4" fill="none"/></symbol>
    <symbol id="i-backspace" viewBox="0 0 30 20"><path d="M7 3l-6 7 6 7" fill="none" stroke="currentColor" stroke-width="1.4"/><path d="M13 4l12 12M25 4L13 16" stroke="currentColor" stroke-width="1.4"/></symbol>
    <symbol id="menu-art" viewBox="0 0 320 560">
      <rect x="150" y="160" width="130" height="120" fill="var(--blue-tile)" opacity=".6"/>
      <rect x="30" y="230" width="130" height="120" fill="var(--blue-tile)" opacity=".6"/>
      <rect x="80" y="345" width="130" height="120" fill="var(--blue-tile)" opacity=".6"/>
      <circle cx="215" cy="220" r="56" fill="none" stroke="var(--ring)" stroke-width="4"/>
      <circle cx="95" cy="292" r="56" fill="none" stroke="var(--ring)" stroke-width="4"/>
      <circle cx="145" cy="405" r="56" fill="none" stroke="var(--ring)" stroke-width="4"/>
      <path d="M158 318h26M171 305v26" stroke="var(--ring)" stroke-width="2"/>
      <text x="215" y="217" font-size="26" font-weight="300" fill="#fff" text-anchor="middle" font-family="Jost,sans-serif">?</text>
      <text x="215" y="240" class="menu-label">chiedere</text>
      <use href="#i-hand" x="82" y="262" width="26" height="26" color="#fff"/>
      <text x="95" y="310" class="menu-label">acquistare</text>
      <use href="#i-user" x="133" y="378" width="24" height="24" color="#fff"/>
      <text x="145" y="424" class="menu-label">conto</text>
    </symbol>
  </defs>
</svg>

<!-- Screen 1: home -->
<section class="screen screen--home">
  <div class="status-bar"><span class="signal">●●●○○ LUMA</span><span>4:21 PM</span><span class="battery">22% <i class="battery-icon"></i></span></div>
  <div class="top-bar">
    <svg class="icon-user" width="18" height="18" color="#cfe3fb"><use href="#i-user"/></svg>
    <svg class="menu-caret" width="16" height="12"><path d="M1 1h14L8 11z" fill="none" stroke="#cfe3fb" stroke-width="1.5"/></svg>
    <svg class="icon-gear" width="18" height="18" color="#4da3f2"><use href="#i-gear"/></svg>
  </div>
  <p class="welcome">benvenuto a</p>
  <div class="brand brand--large"><span class="brand-dot"></span>Zentro</div>
  <div class="brand-rule"></div>
  <svg class="menu-graphic" width="320" height="560">
    <use href="#menu-art"/>
    <circle cx="245" cy="335" r="56" fill="none" stroke="var(--ring)" stroke-width="4"/>
    <use href="#i-cart" x="232" y="308" width="26" height="26" color="#fff"/>
    <text x="245" y="355" class="menu-label">spaccio</text>
  </svg>
  <div class="footer-bars"><span></span><span></span><span></span></div>
</section>

<!-- Screen 2: home with shop selected -->
<section class="screen screen--shop">
  <div class="status-bar"><span class="signal">●●●○○ LUMA</span><span>4:21 PM</span><span class="battery">22% <i class="battery-icon"></i></span></div>
  <div class="top-bar">
    <svg class="icon-user" width="18" height="18" color="#cfe3fb"><use href="#i-user"/></svg>
    <svg class="menu-caret" width="16" height="12"><path d="M1 1h14L8 11z" fill="none" stroke="#cfe3fb" stroke-width="1.5"/></svg>
    <svg class="icon-gear" width="18" height="18" color="#4da3f2"><use href="#i-gear"/></svg>
  </div>
  <p class="welcome">benvenuto a</p>
  <div class="brand brand--large"><span class="brand-dot"></span>Zentro</div>
  <div class="brand-rule"></div>
  <svg class="menu-graphic" width="320" height="560">
    <use href="#menu-art"/>
    <rect x="175" y="262" width="145" height="148" fill="var(--blue-accent)"/>
    <circle cx="248" cy="335" r="58" fill="none" stroke="#d7ebff" stroke-width="4"/>
    <use href="#i-cart" x="235" y="308" width="26" height="26" color="#fff"/>
    <text x="248" y="355" class="menu-label">spaccio</text>
  </svg>
  <div class="footer-bars"><span></span><span></span><span></span></div>
</section>

<!-- Screen 3: buy -->
<section class="screen screen--buy">
  <div class="status-bar"><span class="signal">●●●○○ LUMA</span><span>4:21 PM</span><span class="battery">22% <i class="battery-icon"></i></span></div>
  <div class="top-bar">
    <svg class="icon-user" width="18" height="18" color="#cfe3fb"><use href="#i-user"/></svg>
    <p class="back-link">◁ Indietro</p>
    <svg class="icon-gear" width="18" height="18" color="#4da3f2"><use href="#i-gear"/></svg>
  </div>
  <div class="block corner-tile"></div>
  <div class="title-row">
    <span class="title-icon"><svg width="30" height="30" color="#fff"><use href="#i-hand"/></svg></span>
    <span class="divider"></span><span class="title">acquistare</span>
  </div>
  <div class="block tab-phone">Cellulare</div>
  <div class="block field-phone">6</div>
  <div class="block prefix">+39</div>
  <div class="block field-amount">€</div>
  <p class="notes-hint">Inserici note (opzionale)</p>
  <div class="keypad">
    <div class="key">1</div>
    <div class="key">2<small>ABC</small></div>
    <div class="key">3<small>DEF</small></div>
    <div class="key">4<small>GHI</small></div>
    <div class="key">5<small>JKL</small></div>
    <div class="key key--active">6<small>MNO</small></div>
    <div class="key">7<small>PQRS</small></div>
    <div class="key">8<small>TUV</small></div>
    <div class="key">9<small>WXYZ</small></div>
    <div class="key key--empty"></div>
    <div class="key">0</div>
    <div class="key"><svg width="30" height="20" color="#fff"><use href="#i-backspace"/></svg></div>
  </div>
  <div class="brand brand--small"><span class="brand-dot"></span>Zentro</div>
  <div class="footer-bars"><span></span><span></span><span></span></div>
</section>

<!-- Screen 4: balance -->
<section class="screen screen--balance">
  <div class="status-bar"><span class="signal">●●●○○ LUMA</span><span>4:21 PM</span><span class="battery">22% <i class="battery-icon"></i></span></div>
  <div class="top-bar">
    <svg class="icon-user" width="18" height="18" color="#cfe3fb"><use href="#i-user"/></svg>
    <p class="back-link">◁ Indietro</p>
    <svg class="icon-gear" width="18" height="18" color="#4da3f2"><use href="#i-gear"/></svg>
  </div>
  <div class="block balance-tile">0,00</div>
  <div class="title-row">
    <span class="title-icon"><svg width="32" height="28" color="#fff"><use href="#i-user-clock"/></svg></span>
    <span class="divider"></span><span class="title">il tue saldo</span>
  </div>
  <div class="block band"><i class="caret" style="color:#b8dafa"></i></div>
  <div class="block currency">€</div>
  <div class="block period">Ultimi 30 giorni</div>
  <div class="block tx-row tx-row--in">
    <svg width="22" height="22" color="#0f3262"><use href="#i-house"/></svg>
    <span>+39355501010</span><span class="amount">€ 1</span><i class="caret"></i>
  </div>
  <div class="block tx-row tx-row--out">
    <svg width="22" height="22" color="#fff"><use href="#i-house"/></svg>
    <span>+39355501010</span><span class="amount">€ -1</span><i class="caret"></i>
  </div>
  <div class="brand brand--small"><span class="brand-dot"></span>Zentro</div>
  <div class="footer-bars"><span></span><span></span><span></span></div>
</section>

</body>
</html>
```